Non-Fiction Book On Creativity - Cover Design / Physical and E-Book

I am looking for designs for my first book! It's called: Patience Builds Harbors. The subtitle is: 12 Chapters About Gathering Courage, Mending Fences, And Walking A Quiet Road.
It's a series of short lessons and principals on creativity and it will be a Vellora book and a physical book.
I'm really open to any type of designs but have attached some screenshots of other book covers that have a design and style that I like.
Please let me know if you have any questions or need any more information.
Creativity / Self-Help / Personal Development

```html
<!DOCTYPE html>
<html lang="en">
<head>
<meta charset="UTF-8">
<title>Patience Builds Harbors — Book Cover</title>
<link href="https://fonts.googleapis.com/css2?family=Archivo:wght@400;700;800;900&display=swap" rel="stylesheet">
<style>
  :root {
    --page-bg: #f4f4f4;
    --title-red: #e0062a;
    --title-navy: #0d4378;
    --text-dark: #111111;
    --sky-pink: #efcaf8;
    --sky-white: #faf5ff;
    --sky-blue: #a9dcf6;
    --band-violet: #b48af0;
    --band-lilac: #d9c7fa;
    --band-blue: #3fb1ec;
    --suit-dark: #1b1c22;
    --suit-mid: #3a3c45;
  }
  * { margin: 0; padding: 0; box-sizing: border-box; }
  html, body {
    width: 1200px;
    height: 800px;
    overflow: hidden;
    background: var(--page-bg);
    font-family: "Archivo", Arial, sans-serif;
  }
  .canvas {
    position: relative;
    width: 1200px;
    height: 800px;
  }
  .cover {
    position: absolute;
    left: 375px;
    top: 40px;
    width: 450px;
    height: 720px;
    overflow: hidden;
    background: linear-gradient(100deg, var(--sky-pink) 0%, var(--sky-white) 42%, var(--sky-blue) 100%);
    box-shadow: 0 10px 30px rgba(0,0,0,0.12);
  }
  .wave-band {
    position: absolute;
    left: 0;
    top: 260px;
    width: 450px;
    height: 240px;
  }
  .cover-photo {
    position: absolute;
    left: 188px;
    top: 210px;
    width: 258px;
    height: 510px;
    background: linear-gradient(180deg, #e4e7ec 0%, #c9ccd3 28%, var(--suit-mid) 40%, var(--suit-dark) 100%);
    border-radius: 110px 110px 0 0;
  }
  .title {
    position: absolute;
    left: 0;
    top: 70px;
    width: 100%;
    text-align: center;
    text-transform: uppercase;
    line-height: 1;
  }
  .title-main {
    display: block;
    color: var(--title-red);
    font-weight: 900;
    font-size: 58px;
    letter-spacing: -0.5px;
  }
  .title-link {
    display: flex;
    align-items: center;
    justify-content: center;
    gap: 8px;
    margin: 10px 0 12px;
    color: var(--title-navy);
    font-weight: 800;
    font-size: 40px;
  }
  .title-link::before,
  .title-link::after {
    content: "";
    display: block;
    width: 66px;
    height: 6px;
    background: var(--title-navy);
  }
  .subtitle {
    position: absolute;
    left: 42px;
    top: 505px;
    width: 150px;
    color: var(--text-dark);
    text-transform: uppercase;
    font-size: 16px;
    line-height: 1.42;
    font-weight: 400;
  }
  .subtitle strong {
    display: block;
    font-weight: 800;
    font-size: 17px;
  }
</style>
</head>
<body>
  <main class="canvas">
    <section class="cover">
      <svg class="wave-band" viewBox="0 0 450 240" aria-hidden="true">
        <defs>
          <linearGradient id="bandFill" x1="0" y1="0" x2="1" y2="0">
            <stop offset="0" stop-color="var(--band-violet)"/>
            <stop offset="0.55" stop-color="var(--band-lilac)"/>
            <stop offset="1" stop-color="var(--band-blue)"/>
          </linearGradient>
        </defs>
        <path d="M0 10 C120 60 300 80 450 20 L450 160 C320 200 160 230 0 230 Z" fill="url(#bandFill)" opacity="0.75"/>
        <path d="M0 40 C140 90 300 100 450 50" fill="none" stroke="#ffffff" stroke-width="2" opacity="0.6"/>
      </svg>

      <div class="cover-photo" role="img" aria-label="Photo of a man in a black suit and white vest whose head is a clear light bulb"></div>

      <h1 class="title">
        <span class="title-main">Patience</span>
        <span class="title-link">Builds</span>
        <span class="title-main">Harbors</span>
      </h1>

      <p class="subtitle">
        <strong>12 Chapters</strong>
        About Gathering Courage, Mending Fences, And Walking A Quiet Road
      </p>
    </section>
  </main>
</body>
</html>
```